Postcard Design/Coupon

My business is a Pizza Shop/Restaurant/Bar. I know confusing. I sell mainly pizza and beer but sandwich's and salads are a big seller also. So I want coupons/postcards that I can hand out to every table that comes in to entice them to come back. I also will be sending these coupons/postcards to delivery customers. The business name is Larkdale Pizza Vento address is 581 Thistle Avenue Sewickley PA15143 phone number is 412-741-1744On one side I wanted the coupon offer and logo and the other side the hours but also room for me to send some out.

Target Market(s)

Families

Industry/Entity Type

Restaurant

Requirements
Must have
• Pizza
Nice to have
• Salads/Hoagies/Nice Description

```html
<!DOCTYPE html>
<html lang="en">
<head>
<meta charset="utf-8">
<title>Larkdale Pizza Vento – Postcard Coupon</title>
<link href="https://fonts.googleapis.com/css2?family=Roboto:wght@400;700;900&family=Oswald:wght@600&display=swap" rel="stylesheet">
<style>
  :root {
    --page: #e9e9e9;
    --red: #c8141d;
    --red-dark: #8f0c12;
    --green: #3f8a2c;
    --green-dark: #3b4f2a;
    --yellow: #ffe41a;
    --orange: #f26522;
    --white: #ffffff;
    --ink: #111111;
    --cheese: #e7a650;
    --crust: #c46a2d;
    --beer: #f2b51f;
  }
  * { box-sizing: border-box; margin: 0; padding: 0; }
  html, body { width: 1200px; height: 1200px; overflow: hidden; }
  body {
    background: var(--page);
    font-family: "Roboto", Arial, sans-serif;
    position: relative;
  }
  .postcard {
    position: absolute;
    left: 210px;
    width: 780px;
    height: 520px;
    overflow: hidden;
    box-shadow: 0 6px 18px rgba(0,0,0,.18);
  }
  .postcard--front { top: 50px; background: radial-gradient(circle at 35% 30%, #e0262b, var(--red) 55%, var(--red-dark)); }
  .postcard--back { top: 630px; background: var(--white); }

  /* front */
  .brand-name {
    position: absolute; left: 90px; top: 50px; width: 330px;
    color: var(--white); font-weight: 900; font-size: 64px; line-height: .95; text-align: center;
  }
  .pizza-photo {
    position: absolute; left: 30px; top: 205px; width: 460px; height: 460px; border-radius: 50%;
    background: radial-gradient(circle, var(--cheese) 0%, #d9833d 60%, var(--crust) 100%);
  }
  .side-photo {
    position: absolute; right: 0; top: 70px; width: 290px; height: 450px;
    background: linear-gradient(180deg, #d9a569 0%, #e9c27a 25%, var(--beer) 55%, #e39a17 100%);
  }
  .info-band {
    position: absolute; left: 0; top: 325px; width: 560px; height: 135px;
    background: var(--green); padding: 16px 0 0 40px; color: var(--white);
  }
  .info-band__name { font-weight: 700; font-size: 19px; text-transform: uppercase; }
  .info-band__address { font-size: 19px; margin-top: 2px; }
  .info-band__phone { color: var(--yellow); font-weight: 900; font-size: 46px; margin-top: 4px; letter-spacing: 1px; }
  .hours-badge {
    position: absolute; right: 30px; top: 255px; text-align: center; color: var(--ink);
    font-family: "Oswald", "Arial Narrow", sans-serif;
  }
  .hours-badge__title { font-size: 38px; line-height: 1; }
  .hours-badge__time { font-size: 20px; }
  .page-curl { position: absolute; right: 0; bottom: 0; width: 140px; height: 110px; }
  .page-curl__text {
    position: absolute; right: 18px; bottom: 12px; width: 70px;
    font-size: 13px; line-height: 1.05; text-transform: uppercase; color: var(--ink);
    transform: rotate(-38deg); text-align: center;
  }

  /* back */
  .offer-panel {
    position: absolute; left: 0; top: 0; width: 370px; height: 425px; background: var(--green-dark);
    overflow: hidden;
  }
  .back-pizza-photo {
    position: absolute; left: -120px; top: -40px; width: 420px; height: 360px; border-radius: 50%;
    background: radial-gradient(circle, var(--cheese), #c5602a 70%, #a9481f);
  }
  .coupon {
    position: absolute; left: 60px; top: 40px; width: 290px; height: 220px;
    background: var(--white); border: 3px dashed #d8d8d8;
  }
  .coupon__amount { position: absolute; left: 14px; top: 6px; font-weight: 900; font-size: 44px; color: var(--ink); line-height: 1; }
  .coupon__amount sup { font-size: 24px; }
  .coupon__amount span { font-size: 28px; }
  .coupon__brand { position: absolute; left: 16px; top: 64px; width: 110px; color: var(--green-dark); font-weight: 700; font-size: 22px; line-height: 1; }
  .coupon__photo {
    position: absolute; right: 8px; top: 14px; width: 150px; height: 150px; border-radius: 50%;
    background: radial-gradient(circle, #e9a04e, #b7442a 60%, #d98c3d);
  }
  .coupon__band {
    position: absolute; left: 0; right: 0; bottom: 0; height: 44px; background: var(--orange);
    color: var(--white); font-weight: 700; font-size: 26px; text-align: center; line-height: 44px;
  }
  .order-info { position: absolute; left: 0; top: 290px; width: 370px; text-align: center; color: var(--white); }
  .order-info__lead { font-size: 22px; }
  .order-info__phone { color: var(--yellow); font-weight: 900; font-size: 38px; letter-spacing: 1px; }
  .order-info__rule { height: 2px; background: var(--white); margin: 16px 20px 8px; }
  .order-info__hours { font-weight: 700; font-size: 17px; letter-spacing: .5px; }
  .order-info__rule--bottom { margin: 8px 20px 0; }
  .return-address {
    position: absolute; left: 370px; top: 0; width: 200px; height: 110px; background: var(--green-dark);
    color: var(--white); padding: 22px 10px 0; font-size: 13px; line-height: 1.25;
    font-style: normal; text-align: center;
  }
  .return-address strong { display: block; font-size: 13px; text-transform: uppercase; }
</style>
</head>
<body>

<section class="postcard postcard--front" aria-label="Postcard front">
  <div class="pizza-photo" role="img" aria-label="Photo of a pepperoni and jalapeño pizza"></div>
  <div class="side-photo" role="img" aria-label="Photo of a sandwich, a glass of beer and a fresh salad"></div>
  <div class="brand-name">Pizza Vento</div>
  <div class="info-band">
    <p class="info-band__name">Larkdale Pizza Vento</p>
    <p class="info-band__address">581 Thistle Avenue Brookhaven PA 15990</p>
    <p class="info-band__phone">412-555-0187</p>
  </div>
  <div class="hours-badge">
    <p class="hours-badge__title">HOURS</p>
    <p class="hours-badge__time">11:00AM – 10:00PM</p>
  </div>
  <svg class="page-curl" viewBox="0 0 140 110" aria-hidden="true">
    <polygon points="140,0 140,110 0,110" fill="#ffffff"/>
    <polygon points="140,0 40,110 60,60" fill="#d6d6d6"/>
  </svg>
  <p class="page-curl__text">Flip for offer</p>
</section>

<section class="postcard postcard--back" aria-label="Postcard back">
  <div class="offer-panel">
    <div class="back-pizza-photo" role="img" aria-label="Photo of a pepperoni pizza"></div>
    <div class="coupon">
      <p class="coupon__amount"><sup>$</sup>5<span>OFF</span></p>
      <p class="coupon__brand">Pizza Vento</p>
      <div class="coupon__photo" role="img" aria-label="Photo of a supreme pizza"></div>
      <p class="coupon__band">ON ANY PIZZA</p>
    </div>
    <div class="order-info">
      <p class="order-info__lead">To Place Orders Call</p>
      <p class="order-info__phone">412-555-0187</p>
      <div class="order-info__rule"></div>
      <p class="order-info__hours">HOURS:&nbsp; 11:00 AM – 10:00 PM</p>
      <div class="order-info__rule order-info__rule--bottom"></div>
    </div>
  </div>
  <address class="return-address">
    <strong>Larkdale Pizza Vento</strong>
    581 Thistle Avenue<br>
    Brookhaven PA 15990<br>
    412-555-0187
  </address>
</section>

</body>
</html>
```